Menu redesign of existing iPhone app Flimmo

We need a design upgrade for a footer menu of an iPhone app. We need to incorporate a new button for competitions/missions and it should be extremely modern and clean. The central button to create a Flimmo cannot be too different as our current users are familiar with its usage.

I have attached screenshots of the curent newsfeed and menu.

Target Market(s)

Photography lovers/ design lovers

Font styles to use
Sans Serif

Requirements
Must have
• Flimmo Button,
• Home button,
• My Profile button,
• Find friends button,
• Notifications button,
• Settings button,
• Missions/Competition Button
Nice to have
• Similar Flimmo button as existing on the app

```html
<!DOCTYPE html>
<html lang="en">
<head>
<meta charset="utf-8">
<title>Footer menu redesign</title>
<link href="https://fonts.googleapis.com/css2?family=Roboto:wght@400;500&display=swap" rel="stylesheet">
<style>
  :root {
    --page-bg: #e6eaee;
    --screen-bg: #ffffff;
    --screen-edge: #14161a;
    --status-text: #222428;
    --nav-top: #70757e;
    --nav-bottom: #262a32;
    --icon: #c9ccd2;
    --icon-dim: #9aa0a8;
    --ring: rgba(255,255,255,0.22);
    --accent: #3aa8de;
    --badge: #e5493c;
    --photo-light: #eef1f3;
    --photo-mid: #a9b3ba;
    --photo-dark: #3c4148;
  }
  * { box-sizing: border-box; margin: 0; padding: 0; }
  html, body { width: 1200px; height: 1026px; overflow: hidden; }
  body {
    background: var(--page-bg);
    font-family: "Roboto", Helvetica, Arial, sans-serif;
    position: relative;
  }
  .screen {
    position: absolute;
    top: 123px;
    width: 440px;
    height: 781px;
    background: var(--screen-bg);
    border: 3px solid var(--screen-edge);
    overflow: hidden;
  }
  .screen--feed { left: 130px; }
  .screen--blank { left: 630px; }

  .feed-photo {
    position: absolute;
    inset: 0;
    background: linear-gradient(180deg, var(--photo-light) 0%, #dfe4e7 22%, var(--photo-mid) 52%, #7d858c 72%, var(--photo-dark) 100%);
  }
  .status-bar {
    position: absolute;
    top: 0; left: 0; right: 0;
    height: 28px;
    display: flex;
    align-items: center;
    justify-content: space-between;
    padding: 0 12px;
    font-size: 12px;
    font-weight: 400;
    color: var(--status-text);
    white-space: nowrap;
    z-index: 2;
  }
  .status-bar .carrier, .status-bar .power { display: flex; align-items: center; gap: 5px; }
  .status-bar .time { font-weight: 500; }

  .footer-nav {
    position: absolute;
    left: 0; right: 0; bottom: 0;
    height: 260px;
    z-index: 2;
  }
  .footer-nav svg { position: absolute; inset: 0; }
  .nav-label { fill: #fff; font-size: 9px; font-weight: 500; }
</style>
</head>
<body>

<!-- Footer menu over a feed post -->
<section class="screen screen--feed">
  <div class="feed-photo" role="img" aria-label="Newsfeed photo of a young woman in a black top and ripped jeans standing by a railing"></div>
  <header class="status-bar">
    <span class="carrier">●●●○○ NOVA
      <svg width="13" height="10" viewBox="0 0 13 10"><path d="M1 4a8 8 0 0 1 11 0M3 6a5 5 0 0 1 7 0M5 8a2 2 0 0 1 3 0" fill="none" stroke="currentColor" stroke-width="1.4"/></svg></span>
    <span class="time">4:21 PM</span>
    <span class="power">
      <svg width="7" height="11" viewBox="0 0 7 11"><path d="M1 3l5 5-2.5 2V1L6 3 1 8" fill="none" stroke="currentColor" stroke-width="0.9"/></svg>
      100%
      <svg width="26" height="10" viewBox="0 0 26 10"><rect x="0.5" y="0.5" width="23" height="9" rx="1.5" fill="none" stroke="currentColor"/><rect x="2" y="2" width="20" height="6" fill="currentColor"/><rect x="24" y="3" width="1.5" height="4" fill="currentColor"/></svg>
    </span>
  </header>
  <nav class="footer-nav" aria-label="Main menu">
    <svg width="440" height="260" viewBox="0 0 440 260">
      <defs>
        <linearGradient id="navFeed" x1="0" y1="0" x2="0" y2="1">
          <stop offset="0" stop-color="#3a3f47" stop-opacity="0.35"/>
          <stop offset="0.55" stop-color="#2c313a" stop-opacity="0.85"/>
          <stop offset="1" stop-color="#262a32"/>
        </linearGradient>
      </defs>
      <path d="M0 156 Q220 50 440 156 V260 H0 Z" fill="url(#navFeed)"/>
      <g class="nav-primary">
        <circle cx="118" cy="156" r="20" fill="none" stroke="var(--ring)"/>
        <path d="M118 166V146M111 153l7-7 7 7" fill="none" stroke="var(--icon)" stroke-width="1.5"/>
        <circle cx="220" cy="154" r="33" fill="rgba(0,0,0,0.12)" stroke="var(--ring)"/>
        <path d="M220 140l12 7v14l-12 7-12-7v-14z" fill="var(--accent)"/>
        <circle cx="327" cy="156" r="20" fill="none" stroke="var(--ring)"/>
        <path d="M317 157l10-9 10 9M320 155v8h4v-5h6v5h4v-8" fill="var(--icon)" stroke="var(--icon)" stroke-width="1.2"/>
      </g>
      <line x1="40" y1="197" x2="400" y2="197" stroke="rgba(255,255,255,0.08)"/>
      <g class="nav-secondary" fill="var(--icon-dim)">
        <circle cx="71" cy="220" r="5"/>
        <path d="M62 234a9 8 0 0 1 18 0z"/>
        <circle cx="161" cy="223" r="6" fill="none" stroke="var(--icon-dim)" stroke-width="2"/>
        <path d="M165 227l6 6" stroke="var(--icon-dim)" stroke-width="2.4"/>
        <path d="M263 232h16l-2-3v-6a6 6 0 0 0-12 0v6z"/>
        <circle cx="271" cy="235" r="2"/>
        <circle cx="279" cy="218" r="5" fill="var(--badge)"/>
        <text x="279" y="221" text-anchor="middle" class="nav-label">2</text>
        <circle cx="369" cy="225" r="6" fill="none" stroke="var(--icon-dim)" stroke-width="4" stroke-dasharray="2.4 2.3"/>
        <circle cx="369" cy="225" r="5" fill="none" stroke="var(--icon-dim)" stroke-width="3"/>
      </g>
    </svg>
  </nav>
</section>

<!-- Footer menu on an empty screen -->
<section class="screen screen--blank">
  <header class="status-bar">
    <span class="carrier">●●●○○ NOVA
      <svg width="13" height="10" viewBox="0 0 13 10"><path d="M1 4a8 8 0 0 1 11 0M3 6a5 5 0 0 1 7 0M5 8a2 2 0 0 1 3 0" fill="none" stroke="currentColor" stroke-width="1.4"/></svg></span>
    <span class="time">4:21 PM</span>
    <span class="power">
      <svg width="7" height="11" viewBox="0 0 7 11"><path d="M1 3l5 5-2.5 2V1L6 3 1 8" fill="none" stroke="currentColor" stroke-width="0.9"/></svg>
      100%
      <svg width="26" height="10" viewBox="0 0 26 10"><rect x="0.5" y="0.5" width="23" height="9" rx="1.5" fill="none" stroke="currentColor"/><rect x="2" y="2" width="20" height="6" fill="currentColor"/><rect x="24" y="3" width="1.5" height="4" fill="currentColor"/></svg>
    </span>
  </header>
  <nav class="footer-nav" aria-label="Main menu">
    <svg width="440" height="260" viewBox="0 0 440 260">
      <defs>
        <linearGradient id="navBlank" x1="0" y1="0" x2="0" y2="1">
          <stop offset="0" stop-color="var(--nav-top)"/>
          <stop offset="1" stop-color="var(--nav-bottom)"/>
        </linearGradient>
      </defs>
      <path d="M0 156 Q220 50 440 156 V260 H0 Z" fill="url(#navBlank)"/>
      <g class="nav-primary">
        <circle cx="118" cy="156" r="20" fill="none" stroke="var(--ring)"/>
        <path d="M118 166V146M111 153l7-7 7 7" fill="none" stroke="var(--icon)" stroke-width="1.5"/>
        <circle cx="220" cy="154" r="33" fill="rgba(0,0,0,0.1)" stroke="var(--ring)"/>
        <path d="M220 140l12 7v14l-12 7-12-7v-14z" fill="var(--accent)"/>
        <circle cx="327" cy="156" r="20" fill="none" stroke="var(--ring)"/>
        <path d="M317 157l10-9 10 9M320 155v8h4v-5h6v5h4v-8" fill="var(--icon)" stroke="var(--icon)" stroke-width="1.2"/>
      </g>
      <line x1="40" y1="197" x2="400" y2="197" stroke="rgba(255,255,255,0.08)"/>
      <g class="nav-secondary" fill="var(--icon-dim)">
        <circle cx="71" cy="220" r="5"/>
        <path d="M62 234a9 8 0 0 1 18 0z"/>
        <circle cx="161" cy="223" r="6" fill="none" stroke="var(--icon-dim)" stroke-width="2"/>
        <path d="M165 227l6 6" stroke="var(--icon-dim)" stroke-width="2.4"/>
        <path d="M263 232h16l-2-3v-6a6 6 0 0 0-12 0v6z"/>
        <circle cx="271" cy="235" r="2"/>
        <circle cx="279" cy="218" r="5" fill="var(--badge)"/>
        <text x="279" y="221" text-anchor="middle" class="nav-label">2</text>
        <circle cx="369" cy="225" r="6" fill="none" stroke="var(--icon-dim)" stroke-width="4" stroke-dasharray="2.4 2.3"/>
        <circle cx="369" cy="225" r="5" fill="none" stroke="var(--icon-dim)" stroke-width="3"/>
      </g>
    </svg>
  </nav>
</section>

</body>
</html>
```